Business Card Design Project

Name Martin Holroyd
Company Veldmark Site Restoration Crew
address 22/7 Penbrook street
Wattle Downs
Brisbane Queensland
Australia 4110,
0498357261

Things that we do Mould inspection and Remediation,
Crime and Trauma Scene Cleanup and Decontamination
Drug lab Decontamination and needle cleanups.
Odor control
Air quality Testing and swabs,
latest equipment
Hydroxyl machines, ozone machines ,Sterilising lights ,Comercial Steam machines ,
Thermal imaging, Bacteria testing equipment
Fully trained personel

Reason: One day is not enough time to get designs i dont why the Current deadline is only one day

I do not need purovex in the cards, that was only a sample, The Business name isĀ 

Veldmark Site Restoration Crew.

Target Market(s)

Government agencies ,Police and real-estates, housing companies, Coroners

Industry/Entity Type

Business

Requirements
Must have
• Must tell what we are about
Nice to have
• raised letters or good background

```html
<!DOCTYPE html>
<html lang="en">
<head>
<meta charset="utf-8">
<title>Martin Holroyd – Veldmark Site Restoration Crew</title>
<link href="https://fonts.googleapis.com/css2?family=Cinzel:wght@400;600&family=Didact+Gothic&display=swap" rel="stylesheet">
<style>
  :root {
    --page-bg: #f1f1f1;
    --card-black: #050505;
    --card-glow: #6a6a6a;
    --card-mid: #1c1c1c;
    --ink-white: #ffffff;
    --ink-soft: #e6e6e6;
    --hazard-yellow: #f2d21a;
  }
  html, body {
    margin: 0;
    width: 1200px;
    height: 1197px;
    overflow: hidden;
    background: var(--page-bg);
  }
  .business-card {
    position: absolute;
    left: 90px;
    top: 278px;
    width: 1020px;
    height: 640px;
    border-radius: 44px;
    overflow: hidden;
    background:
      radial-gradient(ellipse 520px 380px at 600px 290px, var(--card-glow) 0%, var(--card-mid) 55%, var(--card-black) 100%);
    font-family: "Didact Gothic", "Century Gothic", sans-serif;
    color: var(--ink-white);
  }
  .brand-mark {
    position: absolute;
    left: 84px;
    top: 150px;
    width: 290px;
    display: flex;
    align-items: center;
    gap: 20px;
  }
  .brand-dot {
    flex: 0 0 64px;
    height: 64px;
    border-radius: 50%;
    background: var(--hazard-yellow);
  }
  .brand-name {
    font-size: 27px;
    line-height: 1.25;
    color: var(--ink-white);
  }
  .holder {
    position: absolute;
    left: 590px;
    top: 78px;
  }
  .holder-name {
    margin: 0;
    font-family: "Cinzel", "Times New Roman", serif;
    font-weight: 600;
    font-size: 50px;
    letter-spacing: 1px;
    line-height: 1;
    color: var(--ink-white);
  }
  .holder-company {
    margin: 16px 0 0;
    font-size: 28px;
    line-height: 37px;
    color: var(--ink-soft);
  }
  .contact-list {
    position: absolute;
    left: 90px;
    top: 400px;
    margin: 0;
    padding: 0;
    list-style: none;
  }
  .contact-item {
    display: flex;
    align-items: center;
    height: 48px;
    font-size: 32px;
    color: var(--ink-white);
  }
  .contact-item.email {
    margin-top: 9px;
    font-size: 29px;
  }
  .contact-icon {
    width: 34px;
    height: 30px;
    margin-right: 24px;
    fill: var(--ink-white);
  }
  .address {
    position: absolute;
    left: 590px;
    top: 398px;
    margin: 0;
    font-style: normal;
    font-size: 30px;
    line-height: 37px;
    color: var(--ink-white);
  }
</style>
</head>
<body>
  <section class="business-card">
    <div class="brand-mark">
      <span class="brand-dot"></span>
      <span class="brand-name">Veldmark Site<br>Restoration Crew</span>
    </div>

    <header class="holder">
      <h1 class="holder-name">Martin Holroyd</h1>
      <p class="holder-company">Veldmark Site<br>Restoration Crew</p>
    </header>

    <ul class="contact-list">
      <li class="contact-item phone">
        <svg class="contact-icon" viewBox="0 0 34 30" aria-hidden="true">
          <path d="M3 9c0-4 6-6 14-6s14 2 14 6v3h-7V9c-2-1-4-1.3-7-1.3S12 8 10 9v3H3z"/>
          <path d="M9 13h16l4 14H5z"/>
          <circle cx="17" cy="20" r="3.5" fill="#111"/>
        </svg>
        049 8357261
      </li>
      <li class="contact-item fax">
        <svg class="contact-icon" viewBox="0 0 34 30" aria-hidden="true">
          <rect x="9" y="2" width="16" height="8"/>
          <rect x="2" y="11" width="30" height="11" rx="2"/>
          <rect x="9" y="19" width="16" height="9" stroke="#111" stroke-width="1.5"/>
        </svg>
        617 30418826
      </li>
      <li class="contact-item email">
        <svg class="contact-icon" viewBox="0 0 34 30" aria-hidden="true">
          <rect x="3" y="6" width="28" height="19" fill="none" stroke="#fff" stroke-width="2.6"/>
          <path d="M3 6l14 11 14-11" fill="none" stroke="#fff" stroke-width="2.6"/>
        </svg>
        martin@veldmarkrestore.com.au
      </li>
    </ul>

    <address class="address">
      22/7 Penbrook street<br>
      Wattle Downs<br>
      Brisbane Queensland<br>
      Australia 4110
    </address>
  </section>
</body>
</html>
```